Create a Brochure Design for Harlow Senior Living

Harlow Senior Living is a subsidiary of the Harlow Care Group. This brochure is specifically for the Harlow Senior Living company and brand. Create a 3 panel, front and back, tri-fold brochure. This brochure will be a way to introduce our senior living care home to the community, prospective, clients, and various referral partners. It is modern and state of the art home. Like the home, the brochure must be eye catching, unique in its deliverables (as it doesn’t feel like a care facility) and demonstrate both attention to detail and comfort. Our organization is sophisticated and built around warmth, care and individualized personal attention. The most important aspect of this design is to focus on creating a nurturing, warm, and inviting feel where you would want to put your own loved ones in our care home.
I am open to the creativity of the designer to develop something based on the above criteria; however I would like the design to work well with the existing collateral material. What I mean by that is that while I want everything to have its own personality and stand out as its own brand representative, I still need to be able to tell that the overall design concept stays stylistically inside of the same ‘family’ of existing designed material. Because of this, below I would like for the designer to pull inspiration from the link to our website (Located below) as well as from the attachment of our recently refreshed business cards (Attached). This should allow each design to be unique and creative, while still staying inside of a framework and the feel/style that I am looking for.
Finally, I want all the designers to understand that this brochure design is for a facility where we are responsible to provide care for active, positive, and happy seniors/elders. We have care professionals and staff on-site to provide 24x7, around the clock, care to the elders and geriatric residents as it is needed and required. The photos that are used must represent aging gracefully and with elegance.
Target Market(s)
Seniors(50+), Caring Family Members, Social Workers, Physicians, Hospitals
Industry/Entity Type
Business
Requirements
Must have
- • The company logo must be included.
Nice to have
- Attached you will find a sampling of images related to the long term care industry. Please feel free to use your own images as you see fit. The interior care home pictures are of our actual facility and should be incorporated into the brochure and your design.
Company Information
• Look under the Harlow Senior Living tab at
www.harlowcaregroup.example.

```html
<!DOCTYPE html>
<html lang="en">
<head>
<meta charset="utf-8">
<title>Harlow Senior Living – Brochure Outside Panels</title>
<link rel="stylesheet" href="https://fonts.googleapis.com/css2?family=Great+Vibes&family=Noto+Serif:wght@400;700&display=swap">
<style>
  :root {
    --teal-dark: #5a9593;
    --teal-mid: #7fb1b1;
    --teal-light: #a9cfd0;
    --teal-pale: #c9e0e0;
    --paper-top: #d7e5e6;
    --paper-bottom: #eef3f3;
    --ink: #333a3c;
    --logo-ink: #5b5f61;
    --script: #5f9c9a;
    --white: #ffffff;
  }
  * { box-sizing: border-box; margin: 0; padding: 0; }
  html, body { width: 1200px; height: 947px; overflow: hidden; background: var(--white); }
  .brochure {
    position: relative;
    width: 1200px;
    height: 947px;
    overflow: hidden;
    background: linear-gradient(180deg, var(--paper-top) 0%, var(--paper-bottom) 45%, var(--paper-top) 100%);
    font-family: "Noto Serif", Georgia, serif;
    color: var(--ink);
  }
  .artwork { position: absolute; inset: 0; }
  .section-title {
    position: absolute;
    font-family: "Great Vibes", cursive;
    font-weight: 400;
    font-size: 34px;
    color: var(--script);
    text-align: center;
    width: 300px;
  }
  .about-title { left: 35px; top: 210px; }
  .services-title { left: 455px; top: 210px; }
  .panel-copy {
    position: absolute;
    font-size: 13.4px;
    line-height: 17.6px;
    text-align: justify;
    hyphens: auto;
  }
  .about-copy { left: 38px; top: 266px; width: 364px; }
  .services-copy { left: 451px; top: 266px; width: 320px; }
  .brand-mark {
    position: absolute;
    left: 860px;
    top: 212px;
    width: 310px;
    text-align: center;
    color: var(--logo-ink);
    font-family: "Noto Serif", Georgia, serif;
    font-weight: 400;
  }
  .brand-square {
    display: block;
    width: 70px;
    height: 70px;
    margin: 0 auto 10px;
    border-radius: 6px;
    background: var(--teal-mid);
  }
  .brand-name { display: block; font-size: 58px; line-height: 60px; }
  .brand-sub { display: block; font-size: 36px; line-height: 42px; }
  .tagline {
    position: absolute;
    color: var(--white);
    font-family: "Noto Serif", Georgia, serif;
    text-shadow: 0 3px 8px rgba(0, 0, 0, 0.45);
    line-height: 1;
  }
  .tagline-small { display: block; font-size: 30px; font-weight: 400; }
  .tagline-large { display: block; font-size: 70px; font-weight: 700; }
  .tagline-left { left: 145px; top: 688px; }
  .tagline-right { right: 70px; top: 700px; text-align: center; }
  .tagline-right .tagline-large { margin-top: -4px; }
  .contact {
    position: absolute;
    left: 0;
    width: 1212px;
    top: 848px;
    text-align: center;
    color: var(--white);
    font-size: 17.5px;
    line-height: 22px;
    list-style: none;
  }
</style>
</head>
<body>
<main class="brochure">
  <svg class="artwork" width="1200" height="947" viewBox="0 0 1200 947" aria-hidden="false">
    <defs>
      <linearGradient id="bedroomTone" x1="0" y1="0" x2="1" y2="1">
        <stop offset="0" stop-color="#6b4a32"/>
        <stop offset="0.5" stop-color="#c9a47a"/>
        <stop offset="1" stop-color="#3a2a22"/>
      </linearGradient>
      <linearGradient id="loungeTone" x1="0" y1="0" x2="1" y2="1">
        <stop offset="0" stop-color="#e8d6b5"/>
        <stop offset="0.5" stop-color="#a0866a"/>
        <stop offset="1" stop-color="#6b5747"/>
      </linearGradient>
      <linearGradient id="skyTone" x1="0" y1="0" x2="0" y2="1">
        <stop offset="0" stop-color="#cfe4f0"/>
        <stop offset="0.6" stop-color="#b8d3df"/>
        <stop offset="1" stop-color="#d9c9b8"/>
      </linearGradient>
      <linearGradient id="heartRibbon" x1="0" y1="0" x2="0" y2="1">
        <stop offset="0" stop-color="#9cc6c6"/>
        <stop offset="1" stop-color="#6fa5a4"/>
      </linearGradient>
    </defs>

    <!-- top wave bands -->
    <path d="M0 0 H1200 V150 C1000 190 720 130 420 165 C260 185 110 205 0 210 Z" fill="var(--teal-pale)"/>
    <path d="M0 0 H1200 V120 C1000 160 720 100 420 135 C260 155 110 180 0 188 Z" fill="var(--teal-light)"/>
    <path d="M0 0 H1200 V95 C1000 135 720 75 420 110 C260 128 110 150 0 160 Z" fill="var(--teal-mid)"/>
    <path d="M0 0 H1200 V60 C1000 105 720 50 420 85 C260 102 110 110 0 112 Z" fill="var(--teal-dark)"/>

    <!-- mid wave behind photos -->
    <path d="M0 505 C200 470 400 470 600 480 C800 490 1000 440 1200 430 V470 C1000 480 800 520 600 515 C400 510 200 505 0 540 Z" fill="var(--teal-light)"/>

    <!-- photo areas -->
    <path role="img" aria-label="Photo: elegant resident bedroom with dark wood furniture and a sunny balcony" d="M0 525 C140 500 280 492 420 495 L420 770 C280 770 140 775 0 790 Z" fill="url(#bedroomTone)"/>
    <path role="img" aria-label="Photo: spacious lounge with sectional sofa, red cushions and bright windows" d="M800 500 C940 475 1080 460 1200 450 V745 C1080 752 940 760 800 765 Z" fill="url(#loungeTone)"/>

    <!-- bottom wave bands -->
    <path d="M0 770 C250 740 500 745 700 755 C900 765 1050 740 1200 725 V947 H0 Z" fill="var(--teal-pale)"/>
    <path d="M0 790 C250 765 500 770 700 780 C900 790 1050 768 1200 755 V947 H0 Z" fill="var(--teal-light)"/>
    <path d="M0 815 C250 795 500 800 700 805 C900 812 1050 800 1200 790 V947 H0 Z" fill="var(--teal-mid)"/>
    <path d="M0 845 C250 830 500 832 700 835 C900 838 1050 830 1200 822 V947 H0 Z" fill="var(--teal-dark)"/>

    <!-- heart frame -->
    <path d="M610 488 C565 385 392 365 385 472 C380 572 530 640 610 748 C690 640 840 572 835 472 C828 365 655 385 610 488 Z" fill="url(#heartRibbon)" stroke="var(--white)" stroke-width="5"/>
    <path role="img" aria-label="Photo: smiling senior couple riding bicycles outdoors" d="M610 512 C572 425 442 412 437 488 C434 560 542 612 610 692 C678 612 786 560 783 488 C778 412 648 425 610 512 Z" fill="url(#skyTone)" stroke="var(--white)" stroke-width="4"/>
  </svg>

  <h2 class="section-title about-title">About us</h2>
  <p class="panel-copy about-copy">Harlow Care Group is proud to usher in a new era in long-term care - Harlow Senior Living. Harlow Senior Living was developed as a response to innumerable requests from our clients for assistance locating suitable homes or facilities when in-home care is no longer appropriate. Now, your care can remain with the best!</p>

  <h2 class="section-title services-title">Services</h2>
  <p class="panel-copy services-copy">Harlow Senior Living is a unique care concept, designed around a social model which encourages “neighbors” to be as independent as possible, actively participate in life here, and interact with their fellow neighbors.</p>

  <div class="brand-mark">
    <span class="brand-square"></span>
    <span class="brand-name">Harlow</span>
    <span class="brand-sub">Senior Living</span>
  </div>

  <p class="tagline tagline-left">
    <span class="tagline-small">It’s a great</span>
    <span class="tagline-large">Life</span>
  </p>
  <p class="tagline tagline-right">
    <span class="tagline-small">Welcome</span>
    <span class="tagline-large">home!</span>
  </p>

  <ul class="contact">
    <li>Tel 808-555-0142</li>
    <li>Fax 808-555-0178</li>
    <li>e-mail: info@harlowcare.example</li>
  </ul>
</main>
</body>
</html>
```